Australian Software Consultancy needs new Business Card Design

Design Business Card based on existing design artefacts (attached). We are open to all designs. As its a 2 sided design and we thought it might be quite striking to have one side with a black background and te other side with a white background.

Target Market(s)

Financial Services mainly.

Industry/Entity Type

Business

Contact Information for Business Card

Name :
Position :
Email :

Requirements
Must have
• Funky design using our existing assets

```html
<!DOCTYPE html>
<html lang="en">
<head>
<meta charset="utf-8">
<title>Bright Ledger – Business Card</title>
<link rel="stylesheet" href="https://fonts.googleapis.com/css2?family=Roboto:wght@400;500;700&display=swap">
<style>
  :root {
    --stage: #2a2a2a;
    --card-black: #0b0b0b;
    --card-white: #ffffff;
    --brand-red: #e8202a;
    --ink: #111111;
    --text-light: #ffffff;
    --ring-faint: rgba(232, 32, 42, 0.28);
  }
  * { margin: 0; padding: 0; box-sizing: border-box; }
  html, body {
    width: 1200px; height: 886px; overflow: hidden;
    background: var(--stage);
    font-family: "Roboto", Arial, sans-serif;
  }
  .canvas { position: relative; width: 1200px; height: 886px; }
  .card {
    position: absolute; width: 540px; height: 310px;
    border-radius: 18px; overflow: hidden;
  }

  /* Back side */
  .card-back {
    left: 70px; top: 120px; background: var(--card-black);
    display: flex; flex-direction: column; align-items: center; justify-content: center;
  }
  .back-ring {
    position: absolute; left: 50%; top: 50%;
    width: 250px; height: 250px; margin: -125px 0 0 -125px;
    border: 22px solid var(--ring-faint); border-radius: 50%;
  }
  .back-wordmark {
    position: relative; color: var(--text-light);
    font-weight: 700; font-size: 42px; letter-spacing: 1px;
  }
  .back-web {
    position: relative; color: var(--text-light);
    font-size: 13px; letter-spacing: 7px; margin-top: 4px;
  }

  /* Front side */
  .card-front { left: 590px; top: 440px; background: var(--card-white); }
  .front-brand {
    height: 150px; display: flex; align-items: center; justify-content: center; gap: 14px;
  }
  .brand-dot { width: 56px; height: 56px; border-radius: 50%; background: var(--brand-red); }
  .brand-name { color: var(--ink); font-weight: 700; font-size: 38px; letter-spacing: 1px; }
  .front-band {
    height: 62px; background: var(--brand-red); color: var(--text-light);
    display: flex; flex-direction: column; align-items: center; justify-content: center;
  }
  .person-name { font-weight: 700; font-size: 22px; letter-spacing: 1px; line-height: 1.1; }
  .person-role { font-size: 16px; line-height: 1.2; }
  .front-contacts {
    height: 98px; background: var(--card-black); color: var(--text-light);
    display: flex; flex-direction: column; align-items: center; justify-content: center;
    font-size: 15px; line-height: 1.5; gap: 1px;
  }
  .contact-label { color: var(--brand-red); }
</style>
</head>
<body>
<div class="canvas">
  <section class="card card-back">
    <div class="back-ring"></div>
    <div class="back-wordmark">BRIGHT LEDGER</div>
    <div class="back-web">www.brightledger.io</div>
  </section>

  <section class="card card-front">
    <div class="front-brand">
      <div class="brand-dot"></div>
      <div class="brand-name">BRIGHT LEDGER</div>
    </div>
    <div class="front-band">
      <div class="person-name">CORIN VALE</div>
      <div class="person-role">CEO/Founder</div>
    </div>
    <div class="front-contacts">
      <div class="contact-line">1420 Harbor Street, Juneau, Alaska 99801</div>
      <div class="contact-line"><span class="contact-label">Phone:</span> 555 214 7730 <span class="contact-label">Mobile:</span> 555 382 6015 <span class="contact-label">Fax:</span> 555 907 4418</div>
      <div class="contact-line"><span class="contact-label">Email:</span> corin@brightledger.io <span class="contact-label">Web:</span> www.brightledger.io</div>
    </div>
  </section>
</div>
</body>
</html>
```